VOLTA NUB (Disposable Charger) Needs packaging with actual mock up!

We have a word document with all the information that we need on the package so feel free to be creative and design your own. It is a small condom wrapper for a one-time use phone charger.

Below I have attached the file with the dimensions of the package. And also some competitors packaging for examples only. Please don't copy them. We need to be different and cooler.

Our logo is also below called Volta Nub(See charger for logo we want). The other ones are just examples.

```html
<!DOCTYPE html>
<html lang="en">
<head>
<meta charset="utf-8">
<title>Volta Nub – Disposable Charger Packaging</title>
<link href="https://fonts.googleapis.com/css2?family=Montserrat:wght@500;600;700;800&family=Lato:wght@400;700&display=swap" rel="stylesheet">
<style>
  :root{
    --green:#6cc276;
    --ink:#1d1d1d;
    --white:#ffffff;
    --grey:#a9a9a9;
    --page:#ffffff;
  }
  *{margin:0;padding:0;box-sizing:border-box}
  html,body{width:1200px;height:648px;overflow:hidden;background:var(--page)}
  body{position:relative;font-family:'Lato',sans-serif;color:var(--ink)}
  .card{position:absolute;background:var(--white);box-shadow:0 1px 4px rgba(0,0,0,.18);overflow:hidden}
  .front{left:59px;top:30px;width:503px;height:589px}
  .back{left:642px;top:33px;width:499px;height:584px}
  .abs{position:absolute}
  .hang{position:absolute}
  .brand-square{position:absolute;background:var(--ink)}
  .wordmark{position:absolute;font-family:'Montserrat',sans-serif;font-weight:700;white-space:nowrap;letter-spacing:1px}
  .front .wordmark{left:0;width:100%;top:118px;text-align:center;font-size:62px;color:var(--green)}
  .headline{position:absolute;left:26px;font-family:'Montserrat',sans-serif;font-weight:800;line-height:1;white-space:nowrap}
  .headline.l1{top:236px;font-size:46px;color:var(--ink)}
  .headline.l2{top:284px;font-size:41px;color:var(--green)}
  .headline.l3{top:325px;font-size:50px;color:var(--ink)}
  .rule{position:absolute;background:var(--green)}
  .ready{position:absolute;left:26px;top:441px;font-family:'Montserrat',sans-serif;font-weight:800;font-size:25px;white-space:nowrap}
  .ready span{color:var(--green)}
  .front-band{position:absolute;left:0;bottom:0;width:100%;height:90px;background:var(--green);color:var(--white);text-align:center;font-family:'Montserrat',sans-serif}
  .front-band .url{position:absolute;top:10px;width:100%;font-size:30px;font-weight:500}
  .front-band .url b{font-weight:700}
  .front-band .tagline{position:absolute;top:52px;width:100%;font-size:21px;font-weight:500}
  .tagline-line{position:absolute;top:65px;height:2px;background:var(--white)}
  .back-header{position:absolute;left:0;top:0;width:100%;height:103px;background:var(--green)}
  .back .wordmark{left:12px;top:37px;font-size:25px;letter-spacing:.5px;color:var(--white)}
  .compat{position:absolute;left:20px;top:123px;font-family:'Montserrat',sans-serif;font-weight:600;font-size:25px}
  .talk{position:absolute;left:379px;top:119px;font-family:'Montserrat',sans-serif;font-weight:600;font-size:14.5px;line-height:18px;color:var(--ink)}
  .talk .hl{color:var(--green)}
  .features{position:absolute;left:0;top:170px;width:100%;height:40px}
  .feature{position:absolute;width:60px;margin-left:-30px;text-align:center;font-size:6px;line-height:6px;color:#777}
  .feature svg{display:block;margin:0 auto 3px}
  .feature.narrow{width:40px;margin-left:-20px}
  .directions{position:absolute;left:20px;top:214px;width:470px;font-size:16.5px;line-height:30px}
  .directions h2{font-family:'Lato',sans-serif;font-weight:700;font-size:22px;color:var(--green);line-height:28px;margin-bottom:2px}
  .directions .num{color:var(--green)}
  .directions .indent{padding-left:16px}
  .caution{position:absolute;left:20px;top:403px;width:470px;font-size:17px;line-height:27px}
  .caution .hl{color:var(--green);font-size:20px}
  .back-url{position:absolute;right:21px;top:460px;font-family:'Montserrat',sans-serif;font-weight:600;font-size:22px;line-height:28px}
  .back-url span{color:var(--green)}
  .cert-band{position:absolute;left:0;bottom:0;width:100%;height:79px;background:var(--ink)}
  .cert{position:absolute;border:3px solid var(--white)}
</style>
</head>
<body>

<section class="card front">
  <div class="brand-square" style="left:19px;top:28px;width:30px;height:30px;"></div>
  <svg class="hang" style="left:172px;top:36px" width="160" height="40" viewBox="0 0 160 40">
    <circle cx="79" cy="18" r="14" fill="#a9a9a9"/>
    <rect x="4" y="25" width="150" height="24" rx="12" fill="#a9a9a9"/>
  </svg>

  <div class="wordmark">VOLTA NUB</div>

  <div class="headline l1">DISPOSABLE</div>
  <div class="headline l2">CELL PHONE</div>
  <div class="headline l3">CHARGER</div>
  <div class="rule" style="left:25px;top:381px;width:249px;height:5px"></div>

  <svg class="abs" style="left:315px;top:263px" width="180" height="180" viewBox="0 0 180 180" aria-label="Capacity badge">
    <defs>
      <path id="arcTop" d="M 22 90 A 68 68 0 0 1 158 90"/>
      <path id="arcBottom" d="M 30 92 A 62 62 0 0 0 150 92"/>
    </defs>
    <circle cx="90" cy="85" r="85" fill="var(--green)"/>
    <circle cx="90" cy="85" r="56" fill="var(--white)"/>
    <rect x="2" y="82" width="16" height="3" fill="var(--ink)"/>
    <text font-family="Montserrat, sans-serif" font-weight="600" font-size="15" fill="var(--ink)" letter-spacing="1">
      <textPath href="#arcTop" startOffset="50%" text-anchor="middle">Compatible with</textPath>
    </text>
    <text font-family="Montserrat, sans-serif" font-weight="600" font-size="15" fill="var(--ink)" letter-spacing="2" dy="14">
      <textPath href="#arcBottom" startOffset="50%" text-anchor="middle">Charged Up</textPath>
    </text>
    <text x="92" y="85" text-anchor="middle" font-family="Montserrat, sans-serif" font-weight="700" font-size="26" fill="var(--green)">2900</text>
    <text x="92" y="111" text-anchor="middle" font-family="Montserrat, sans-serif" font-weight="600" font-size="26" fill="var(--ink)">mAh</text>
  </svg>

  <div class="ready">READY FOR <span>USE</span></div>
  <div class="rule" style="left:26px;top:469px;width:210px;height:2px"></div>
  <div class="abs" style="left:451px;top:453px;width:36px;height:36px;border-radius:50%;background:var(--green)"></div>

  <div class="front-band">
    <div class="url">www.<b>voltanub</b>.com</div>
    <div class="tagline-line" style="left:14px;width:110px"></div>
    <div class="tagline">Bio-degradable shell</div>
    <div class="tagline-line" style="right:14px;width:110px"></div>
  </div>
</section>

<section class="card back">
  <div class="back-header">
    <div class="wordmark">VOLTA NUB</div>
    <svg class="hang" style="left:176px;top:31px" width="160" height="40" viewBox="0 0 160 40">
      <circle cx="73" cy="18" r="14" fill="#fff"/>
      <rect x="0" y="11" width="148" height="24" rx="12" fill="#fff"/>
    </svg>
    <div class="abs" style="left:438px;top:38px;width:30px;height:30px;background:var(--white)"></div>
  </div>

  <div class="compat">Compatible with:</div>
  <svg class="abs" style="left:328px;top:112px" width="44" height="44" viewBox="0 0 44 44">
    <circle cx="21" cy="21" r="18" fill="none" stroke="var(--green)" stroke-width="3.5"/>
    <path d="M14 20 L20 26 L30 14" fill="none" stroke="var(--ink)" stroke-width="2.5"/>
  </svg>
  <div class="talk"><span class="hl">8 HOURS</span> OF<br>TALK TIME</div>

  <div class="features">
    <div class="feature" style="left:29px"><svg width="12" height="14" viewBox="0 0 12 14"><path d="M7 0 L1 8 H6 L4 14 L11 5 H6 Z" fill="var(--green)"/></svg>Pre-Charged</div>
    <div class="feature narrow" style="left:96px"><svg width="14" height="14" viewBox="0 0 14 14"><path d="M2 13 C2 5 7 1 13 1 C13 8 8 12 2 13 Z" fill="var(--green)"/></svg>Biodegradable Shell</div>
    <div class="feature" style="left:159px"><svg width="16" height="12" viewBox="0 0 16 12"><rect x="1" y="2" width="13" height="9" fill="none" stroke="var(--green)" stroke-width="1.5"/><rect x="3" y="4" width="9" height="5" fill="var(--green)"/></svg>1800mAh</div>
    <div class="feature" style="left:217px"><svg width="12" height="14" viewBox="0 0 12 14"><path d="M6 1 C9 5 11 8 11 10 A5 5 0 0 1 1 10 C1 8 3 5 6 1 Z" fill="var(--green)"/></svg>Waterproof</div>
    <div class="feature" style="left:284px"><svg width="14" height="14" viewBox="0 0 14 14"><circle cx="7" cy="7" r="5.5" fill="none" stroke="var(--green)" stroke-width="1.5"/><path d="M7 4 V7 H9.5" fill="none" stroke="var(--green)" stroke-width="1.3"/></svg>3-year shelf life</div>
    <div class="feature" style="left:345px"><svg width="16" height="12" viewBox="0 0 16 12"><rect x="1" y="2" width="13" height="8" rx="1" fill="var(--green)"/><path d="M8 3 L5 7 H8 L7 9 L10 5 H7 Z" fill="#fff"/></svg>Portable</div>
    <div class="feature" style="left:405px"><svg width="12" height="13" viewBox="0 0 12 13"><path d="M1 1 H11 V6 A5 5 0 0 1 1 6 Z" fill="var(--green)"/></svg>Fits in pocket</div>
    <div class="feature narrow" style="left:471px"><svg width="16" height="14" viewBox="0 0 16 14"><rect x="1" y="1" width="6" height="12" rx="1" fill="none" stroke="var(--green)" stroke-width="1.3"/><rect x="9" y="1" width="6" height="12" rx="1" fill="none" stroke="var(--green)" stroke-width="1.3"/></svg>Android<br>iOS + Type C</div>
  </div>

  <div class="directions">
    <h2>Directions:</h2>
    <p><span class="num">1.</span> Plug into your device and switch on pod.</p>
    <p class="indent">(For maximum charge, close all open apps)</p>
    <p><span class="num">2.</span> Pod will charge until light shuts off, or turn off for future use.</p>
    <p><span class="num">3.</span> Please recycle battery, the shell is biodegradable</p>
    <p class="indent">-Total charge varies by device</p>
  </div>

  <div class="caution"><span class="hl">Caution:</span> Don’t get pod wet. Do not disassemble device. Battery may get warm.</div>

  <div class="back-url">www.<span>voltanub</span>.com</div>

  <div class="cert-band">
    <div class="cert" style="left:16px;top:22px;width:38px;height:35px;border-radius:4px"></div>
    <div class="cert" style="left:72px;top:22px;width:38px;height:35px;border-radius:4px"></div>
    <div class="cert" style="left:130px;top:22px;width:40px;height:35px;border-radius:4px"></div>
    <div class="cert" style="left:186px;top:22px;width:36px;height:35px;border-radius:4px"></div>
    <div class="cert" style="left:236px;top:22px;width:34px;height:35px;border-radius:50%"></div>
    <div class="cert" style="left:283px;top:21px;width:36px;height:36px;border-radius:50%"></div>
  </div>
</section>

</body>
</html>
```